COMPANY NAME ------ Velmora22 Brands, Inc. TAGLINE......... Simply Velmora!

I need Graphic design for Coconut oil Skincare products!
I need a graphic design that portrays LUXURY AS APPLIED TO MY COMPANY AND THE TAGLINE ! UPSCALE!!
COLOR LAYOUT ................. GOLD ON BLACK, GOLD ON CHOCOLATE LIKE COLOR!
The designers can focus their graphic design based more the word.." "LUXURY"..... The logo I submitted is the two logo I picked.. the logo and the slogan has to be incorporated in the graphic design... The label has to be "ELEGANT" and " UPSCALE".. It can also be "BOLD".

Target Market(s)

20 - 45 years

Industry/Entity Type

Graphic Design

Font styles to use
Decorative

Requirements
Must have
• Luxury feel to it....
Nice to have
• Logo on the label and oil pouring from inside Coconuts !
Should not have
• Local or Country feel because of the word Coconut oil

```html
<!DOCTYPE html>
<html lang="en">
<head>
<meta charset="utf-8">
<title>NuaNua Coconut Oil Label – Velmora22</title>
<link href="https://fonts.googleapis.com/css2?family=Playfair+Display:wght@700&family=Limelight&family=Oswald:wght@500&display=swap" rel="stylesheet">
<style>
  :root {
    --page: #ffffff;
    --chocolate: #2e0c04;
    --chocolate-soft: #3a1408;
    --gold: #c9943a;
    --gold-light: #f6e2b4;
    --gold-deep: #a8711f;
  }
  html, body {
    margin: 0;
    padding: 0;
    width: 1200px;
    height: 1200px;
    overflow: hidden;
    background: var(--page);
  }
  .canvas {
    position: relative;
    width: 1200px;
    height: 1200px;
  }
  .label {
    position: absolute;
    left: 384px;
    top: 277px;
    width: 432px;
    height: 648px;
    background: var(--chocolate);
    overflow: hidden;
  }
  .label-pattern {
    position: absolute;
    inset: 0;
    background:
      radial-gradient(ellipse at 20% 25%, var(--chocolate-soft) 0%, transparent 45%),
      radial-gradient(ellipse at 80% 60%, var(--chocolate-soft) 0%, transparent 45%),
      radial-gradient(ellipse at 30% 85%, var(--chocolate-soft) 0%, transparent 40%),
      var(--chocolate);
  }
  .brand-mark {
    position: absolute;
    left: 166px;
    top: 52px;
    width: 100px;
    height: 100px;
    border-radius: 50%;
    background: var(--gold);
  }
  .brand {
    position: absolute;
    left: 0;
    width: 100%;
    top: 170px;
    text-align: center;
    color: var(--gold);
    font-family: "Playfair Display", Georgia, serif;
    font-weight: 700;
  }
  .brand-name {
    display: block;
    font-size: 25px;
    letter-spacing: 1.5px;
    line-height: 1;
  }
  .brand-tagline {
    display: block;
    margin-top: 6px;
    font-size: 13px;
    letter-spacing: 0.5px;
  }
  .product-name {
    position: absolute;
    left: 0;
    width: 100%;
    top: 258px;
    margin: 0;
    text-align: center;
    font-family: "Limelight", "Playfair Display", serif;
    font-weight: 400;
    font-size: 72px;
    line-height: 1;
    letter-spacing: -2px;
    transform: scaleY(1.5);
    transform-origin: center top;
    background: linear-gradient(180deg, var(--gold-deep) 0%, var(--gold) 35%, var(--gold-light) 75%, var(--gold) 100%);
    -webkit-background-clip: text;
    background-clip: text;
    color: transparent;
  }
  .product-type {
    position: absolute;
    left: 0;
    width: 100%;
    top: 383px;
    margin: 0;
    text-align: center;
    font-family: "Oswald", "Arial Narrow", sans-serif;
    font-weight: 500;
    font-size: 30px;
    line-height: 1;
    letter-spacing: 0.5px;
    color: var(--gold-light);
  }
  .product-art {
    position: absolute;
    left: 150px;
    top: 477px;
    width: 132px;
    height: 124px;
  }
</style>
</head>
<body>
  <main class="canvas">
    <section class="label">
      <div class="label-pattern" role="img" aria-label="Faint dark swirl pattern across the chocolate background"></div>
      <div class="brand-mark"></div>
      <div class="brand">
        <span class="brand-name">Velmora22</span>
        <span class="brand-tagline">Simply Velmora!</span>
      </div>
      <h1 class="product-name">NuaNua</h1>
      <p class="product-type">COCONUT OIL</p>
      <svg class="product-art" viewBox="0 0 132 124" role="img" aria-label="Gold illustration of a split coconut with oil and a stoppered oil bottle">
        <defs>
          <linearGradient id="artGold" x1="0" y1="0" x2="0" y2="1">
            <stop offset="0" stop-color="#c9943a"/>
            <stop offset="0.5" stop-color="#f6e2b4"/>
            <stop offset="1" stop-color="#c9943a"/>
          </linearGradient>
        </defs>
        <rect x="0" y="0" width="132" height="124" rx="40" fill="url(#artGold)" opacity="0.85"/>
      </svg>
    </section>
  </main>
</body>
</html>
```